Tidewell Estates Co Business Card design

Tidewell Estates Co is a West Vancouver based boutique brokerage specializing in the marketing and sale of luxury and waterfront real estate.

This card is for Marlon Prevost, Vice-President.

The card should have something modern and unique about. Some sort of gimmick would be nice.

I would like it to use or update the tidewell estates logo visible at www.tidewellestates.example

Very open to any design.

Target Market(s)

humans, the type with money

Industry/Entity Type

Marketing

Requirements
Must have
• The name Marlon Prevost

Company name Tidewell Estates Co

Phone 604-555-0142

Fax 604-555-0187

email marlonprevost@mailbox.example

website www.marlonprevost.example

LOGO

tag line"a fresh approach to real estate in west vancouver"

the attched pic of me if possible
Nice to have
• Something that would make people say "nice card" and not throw it in the garbage immediately, open to ideas
Should not have
• anything that looks like a template

```html
<!DOCTYPE html>
<html lang="en">
<head>
<meta charset="utf-8">
<title>Tidewell Estates Co – Business Card</title>
<link rel="stylesheet" href="https://fonts.googleapis.com/css2?family=Libre+Baskerville:wght@400;700&display=swap">
<style>
  :root {
    --stage: #2a2a2c;
    --card-dark: #050505;
    --card-light: #f1f2f4;
    --ink: #111111;
    --paper-text: #ffffff;
    --frame: #141414;
    --icon-phone: #3f9a3a;
    --icon-fax: #c8262b;
    --icon-mail: #3a3fa0;
    --icon-web: #e2a43a;
    --photo-light: #e9e5dc;
    --photo-coat: #c9b898;
    --photo-shirt: #1e2530;
  }
  * { box-sizing: border-box; margin: 0; padding: 0; }
  html, body { width: 1200px; height: 900px; overflow: hidden; }
  body {
    background: var(--stage);
    font-family: "Libre Baskerville", "Times New Roman", serif;
    position: relative;
  }
  .card {
    position: absolute;
    left: 320px;
    width: 560px;
    height: 320px;
    overflow: hidden;
    box-shadow: 0 10px 30px rgba(0,0,0,.45);
  }

  /* Front: black brand side */
  .card--brand { top: 90px; background: var(--card-dark); }
  .brand-lockup {
    position: absolute;
    right: 48px;
    top: 130px;
    text-align: center;
    color: var(--paper-text);
  }
  .brand-lockup__name {
    display: flex; align-items: center; gap: 10px;
    font-size: 24px;
    font-variant: small-caps;
    letter-spacing: .5px;
  }
  .brand-lockup__dot {
    width: 12px; height: 12px; border-radius: 50%;
    background: var(--paper-text);
  }
  .brand-lockup__web {
    margin-top: 8px;
    font-size: 11px;
    letter-spacing: 2px;
  }

  /* Back: white contact side */
  .card--contact { top: 490px; background: var(--card-light); }
  .frame { position: absolute; inset: 0; }
  .portrait {
    position: absolute;
    left: 38px; top: 38px;
    width: 200px; height: 282px;
    background:
      linear-gradient(180deg, transparent 0 38%, var(--photo-coat) 38% 100%),
      var(--photo-light);
  }
  .portrait::after {
    content: "";
    position: absolute;
    left: 74px; top: 108px;
    width: 54px; height: 174px;
    background: var(--photo-shirt);
  }
  .details {
    position: absolute;
    right: 44px; top: 28px;
    width: 250px;
    text-align: right;
    color: var(--ink);
  }
  .details__company {
    display: flex; justify-content: flex-end; align-items: center; gap: 8px;
    font-size: 15px;
    font-variant: small-caps;
    font-weight: 700;
  }
  .details__company-mark {
    width: 9px; height: 9px; background: var(--ink);
  }
  .details__name {
    margin-top: 22px;
    font-size: 24px;
    font-weight: 700;
    font-variant: small-caps;
    letter-spacing: .5px;
    white-space: nowrap;
  }
  .details__title {
    font-size: 15px;
    font-variant: small-caps;
    margin-bottom: 12px;
  }
  .contact-list { list-style: none; font-size: 12px; font-weight: 700; line-height: 1.6; }
  .contact-list li { display: flex; justify-content: flex-end; align-items: center; gap: 6px; white-space: nowrap; }
  .contact-list svg { width: 11px; height: 11px; flex: none; }
</style>
</head>
<body>

<section class="card card--brand" aria-label="Card front">
  <div class="brand-lockup">
    <div class="brand-lockup__name"><span class="brand-lockup__dot"></span>Tidewell Estates Co</div>
    <div class="brand-lockup__web">www.tidewellestates.example</div>
  </div>
</section>

<section class="card card--contact" aria-label="Card back">
  <div class="portrait" role="img" aria-label="Portrait photo of Marlon Prevost in a beige jacket"></div>
  <svg class="frame" viewBox="0 0 560 320" aria-hidden="true">
    <g fill="none" stroke="var(--frame)" stroke-width="2">
      <polyline points="110,18 16,18 16,270"/>
      <polyline points="240,14 540,14 540,262 300,262"/>
    </g>
  </svg>
  <div class="details">
    <div class="details__company"><span class="details__company-mark"></span>Tidewell Estates Co</div>
    <div class="details__name">Marlon Prevost</div>
    <div class="details__title">Vice President</div>
    <ul class="contact-list">
      <li>604-555-0142
        <svg viewBox="0 0 12 12"><rect width="12" height="12" rx="2" fill="var(--icon-phone)"/><rect x="4" y="2" width="4" height="8" rx="1" fill="#fff"/></svg></li>
      <li>604-555-0187
        <svg viewBox="0 0 12 12"><rect width="12" height="12" rx="2" fill="var(--icon-fax)"/><rect x="3" y="5" width="6" height="4" fill="#fff"/></svg></li>
      <li>marlonprevost@mailbox.example
        <svg viewBox="0 0 12 12"><rect y="2" width="12" height="8" fill="var(--icon-mail)"/><polyline points="0,2 6,7 12,2" fill="none" stroke="#fff" stroke-width="1"/></svg></li>
      <li>www.marlonprevost.example
        <svg viewBox="0 0 12 12"><circle cx="6" cy="6" r="5.5" fill="var(--icon-web)"/><circle cx="6" cy="6" r="3" fill="none" stroke="#fff" stroke-width="1"/></svg></li>
    </ul>
  </div>
</section>

</body>
</html>
```